Banners for slider on first page of the website

We need up to 3 different banners for our website: www.trelk.si
Current design is maybe a bit too playful, so do not mind on it. It can include some natural elements
1) Design needs to be modern type
2) Has to include products which are on our website
3) Has to be in two sizes: mobile and web - like we have now
4) Each slider CAN represent each category we have or CAN include multiple
5) Optional text holders

```html
<!DOCTYPE html>
<html lang="sl">
<head>
<meta charset="utf-8">
<title>Trelk – drsnik naslovnice</title>
<link href="https://fonts.googleapis.com/css2?family=Lexend:wght@400;500;600&display=swap" rel="stylesheet">
<style>
:root{
  --pink:#f9a8d4;
  --pink-bar:#f7a1cf;
  --pink-soft:#fde4f0;
  --magenta:#f06fc8;
  --ink:#1f1f24;
  --white:#ffffff;
  --page:#ffffff;
}
*{box-sizing:border-box;margin:0;padding:0}
html,body{width:1200px;height:967px;overflow:hidden;background:var(--page)}
body{position:relative;font-family:"Lexend",sans-serif;color:var(--ink)}

/* desktop banner */
.desk{position:absolute;width:341px;height:171px;background:var(--white);overflow:hidden;box-shadow:0 1px 4px rgba(0,0,0,.08)}
.desk .topbar{height:8px;background:var(--pink-bar);display:flex;align-items:center;justify-content:space-between;padding:0 10px;font-size:3px;color:var(--white);white-space:nowrap}
.desk .topbar .soc{display:flex;gap:3px}
.desk .topbar .soc i{width:3px;height:3px;border-radius:50%;background:var(--white);display:block}
.desk .nav{height:14px;position:relative;display:flex;align-items:center;padding:0 10px;font-size:3px;gap:8px;white-space:nowrap}
.desk .nav .logo{position:absolute;left:50%;transform:translateX(-50%);font-size:5px;font-weight:600;color:var(--magenta);display:flex;align-items:center;gap:1.5px}
.desk .nav .logo::before{content:"";width:4px;height:4px;border-radius:50%;background:var(--magenta)}
.desk .nav .tools{margin-left:auto;display:flex;gap:5px;align-items:center}
.desk .nav .badge{width:3px;height:3px;border-radius:50%;background:var(--pink);display:inline-block;margin-left:1px;vertical-align:middle}
.desk .hero{position:absolute;left:0;top:22px;width:341px;height:134px;background:linear-gradient(100deg,#fff5fa 0%,var(--pink-soft) 45%,#fbd3e8 100%);overflow:hidden}
.desk .arch{position:absolute;left:154px;top:30px;width:150px;height:130px;border-radius:75px 75px 0 0;background:rgba(248,180,218,.45)}
.desk .blob-l{position:absolute;left:-36px;bottom:-36px;width:72px;height:72px;border-radius:50%;background:var(--magenta);opacity:.85}
.desk .blob-r{position:absolute;right:12px;top:52px;width:50px;height:50px;border-radius:50%;background:var(--magenta);opacity:.7}
.desk .blob-t{position:absolute;left:255px;top:16px;width:30px;height:30px;border-radius:50%;background:var(--magenta);opacity:.55}
.desk .photo{position:absolute;left:190px;top:18px;width:110px;height:100px;border-radius:18px}
.desk .copy{position:absolute;left:47px;top:40px;width:125px}
.desk h2{font-size:7.4px;font-weight:600;letter-spacing:.3px;margin-bottom:6px}
.desk p{font-size:5.2px;font-weight:500;line-height:1.25;letter-spacing:.2px}
.desk .btn{display:inline-block;margin-top:9px;background:var(--ink);color:var(--white);font-size:3px;padding:1.8px 3.5px;letter-spacing:.2px;white-space:nowrap}
.dots{position:absolute;display:flex;gap:2px}
.dots i{display:block;border-radius:50%;background:var(--ink)}
.desk .dots{left:168px;bottom:9px}
.desk .dots i{width:3.4px;height:3.4px}
.desk .chat{position:absolute;right:3px;bottom:3px;background:var(--magenta);color:var(--white);font-size:3px;padding:2px 4px;border-radius:3px}

/* mobile banner */
.mob{position:absolute;width:103px;height:196px;background:var(--white);overflow:hidden;box-shadow:0 1px 4px rgba(0,0,0,.1)}
.mob .topbar{height:12px;background:var(--pink-bar);display:flex;justify-content:center;align-items:center;gap:5px}
.mob .topbar i{width:3.5px;height:3.5px;border-radius:50%;background:var(--white);display:block}
.mob .head{height:21px;position:relative;display:flex;align-items:center;justify-content:space-between;padding:0 7px}
.mob .burger{width:6px;height:4px;border-top:1px solid var(--ink);border-bottom:1px solid var(--ink);position:relative}
.mob .burger::after{content:"";position:absolute;left:0;top:0.5px;width:6px;border-top:1px solid var(--ink)}
.mob .logo{font-size:7px;font-weight:600;color:var(--magenta);display:flex;align-items:center;gap:2px}
.mob .logo::before{content:"";width:5px;height:5px;border-radius:50%;background:var(--magenta)}
.mob .cart{width:5px;height:4px;border:1px solid var(--ink);border-radius:0 0 1px 1px;position:relative;margin-right:4px}
.mob .cart::after{content:"";position:absolute;left:6px;top:-1px;width:4px;height:4px;border-radius:50%;background:var(--pink)}
.mob .hero{position:absolute;left:0;top:33px;width:103px;height:122px;background:linear-gradient(160deg,#fff5fa,var(--pink-soft) 50%,#fbd3e8);overflow:hidden}
.mob .blob-r{position:absolute;right:-20px;top:68px;width:44px;height:44px;border-radius:50%;background:var(--magenta);opacity:.8}
.mob .blob-s{position:absolute;right:6px;top:46px;width:16px;height:16px;border-radius:50%;background:var(--magenta);opacity:.7}
.mob .photo{position:absolute;left:19px;top:8px;width:64px;height:54px;border-radius:14px}
.mob .copy{position:absolute;left:6px;right:6px;top:66px;text-align:center}
.mob h2{font-size:4.6px;font-weight:600;margin-bottom:2.5px}
.mob p{font-size:4px;line-height:1.2}
.mob .btn{display:inline-block;margin-top:3px;background:var(--ink);color:var(--white);font-size:2.8px;padding:1.5px 3px;white-space:nowrap}
.mob .dots{left:45px;bottom:4px}
.mob .dots i{width:2.8px;height:2.8px}
.mob .best{position:absolute;left:0;right:0;top:176px;text-align:center;font-size:9px;font-weight:500}

/* product placeholder tones */
.ph-gift{background:radial-gradient(circle at 40% 40%,#7cc8ee,#3e9fd6 60%,#f2c7d6)}
.ph-candle{background:radial-gradient(circle at 45% 50%,#ff5f8f,#d9345f 55%,#e7b85a)}
.ph-shell{background:radial-gradient(circle at 45% 45%,#a8ecef,#5fd0d7 55%,#c9b9e8)}
.ph-balm{background:radial-gradient(circle at 45% 45%,#fbeacd,#f3a3c7 55%,#e9426f)}
.ph-soap{background:radial-gradient(circle at 55% 45%,#fff1a0,#f3d54e 60%,#ec4a94)}
</style>
</head>
<body>

<section class="desk" style="left:48px;top:33px">
  <div class="topbar"><span>info@trelk.si</span><span class="soc"><i></i><i></i></span></div>
  <nav class="nav"><span>Domov</span><span>Trgovina ▾</span><b class="logo">Trelk</b><span class="tools"><span>Vpiši se</span><span>⌕</span><span>♡<span class="badge"></span></span><span>€0,00<span class="badge"></span></span></span></nav>
  <div class="hero">
    <div class="arch"></div><div class="blob-l"></div><div class="blob-t"></div><div class="blob-r"></div>
    <div class="photo ph-gift" role="img" aria-label="Darilni paket z morskimi kopalnimi bombicami"></div>
    <div class="copy"><h2>Darila</h2><p>Darilni Paket Sea Daydream<br>€23,40</p><span class="btn">OGLEJ SI PONUDBO</span></div>
    <div class="dots"><i></i><i></i><i></i></div>
  </div>
  <span class="chat">Klepet</span>
</section>

<section class="desk" style="left:430px;top:33px">
  <div class="topbar"><span>info@trelk.si</span><span class="soc"><i></i><i></i></span></div>
  <nav class="nav"><span>Domov</span><span>Trgovina ▾</span><b class="logo">Trelk</b><span class="tools"><span>Vpiši se</span><span>⌕</span><span>♡<span class="badge"></span></span><span>€0,00<span class="badge"></span></span></span></nav>
  <div class="hero">
    <div class="arch"></div><div class="blob-l"></div><div class="blob-t"></div><div class="blob-r"></div>
    <div class="photo ph-candle" role="img" aria-label="Dišeča sveča v rdeči pločevinki"></div>
    <div class="copy"><h2>Dišave Za Dom</h2><p>Sveča Moonlit Rose 250g<br>€12.40</p><span class="btn">OGLEJ SI PONUDBO</span></div>
    <div class="dots"><i></i><i></i><i></i></div>
  </div>
  <span class="chat">Klepet</span>
</section>

<section class="desk" style="left:808px;top:33px">
  <div class="topbar"><span>info@trelk.si</span><span class="soc"><i></i><i></i></span></div>
  <nav class="nav"><span>Domov</span><span>Trgovina ▾</span><b class="logo">Trelk</b><span class="tools"><span>Vpiši se</span><span>⌕</span><span>♡<span class="badge"></span></span><span>€0,00<span class="badge"></span></span></span></nav>
  <div class="hero">
    <div class="arch"></div><div class="blob-l"></div><div class="blob-t"></div><div class="blob-r"></div>
    <div class="photo ph-shell" role="img" aria-label="Kopalna bombica v obliki školjke"></div>
    <div class="copy"><h2>Kopanje</h2><p>Kopalna Bombica Ocean<br>Shell 160g<br>€5,50</p><span class="btn">OGLEJ SI PONUDBO</span></div>
    <div class="dots"><i></i><i></i><i></i></div>
  </div>
  <span class="chat">Klepet</span>
</section>

<section class="mob" style="left:168px;top:243px">
  <div class="topbar"><i></i><i></i></div>
  <header class="head"><span class="burger"></span><b class="logo">Trelk</b><span class="cart"></span></header>
  <div class="hero"><div class="blob-s"></div><div class="blob-r"></div>
    <div class="photo ph-gift" role="img" aria-label="Darilni paket z morskimi kopalnimi bombicami"></div>
    <div class="copy"><h2>Darila</h2><p>Darilni Paket Sea<br>Daydream<br>€23,40</p><span class="btn">OGLEJ SI PONUDBO</span></div>
    <div class="dots"><i></i><i></i><i></i></div></div>
  <h3 class="best">Najbolj Prodajano</h3>
</section>

<section class="mob" style="left:554px;top:243px">
  <div class="topbar"><i></i><i></i></div>
  <header class="head"><span class="burger"></span><b class="logo">Trelk</b><span class="cart"></span></header>
  <div class="hero"><div class="blob-s"></div><div class="blob-r"></div>
    <div class="photo ph-candle" role="img" aria-label="Dišeča sveča v rdeči pločevinki"></div>
    <div class="copy"><h2>Dišave Za Dom</h2><p>Sveča Moonlit Rose 250g<br>€12.40</p><span class="btn">OGLEJ SI PONUDBO</span></div>
    <div class="dots"><i></i><i></i><i></i></div></div>
  <h3 class="best">Najbolj Prodajano</h3>
</section>

<section class="mob" style="left:928px;top:243px">
  <div class="topbar"><i></i><i></i></div>
  <header class="head"><span class="burger"></span><b class="logo">Trelk</b><span class="cart"></span></header>
  <div class="hero"><div class="blob-s"></div><div class="blob-r"></div>
    <div class="photo ph-shell" role="img" aria-label="Kopalna bombica v obliki školjke"></div>
    <div class="copy"><h2>Kopanje</h2><p>Kopalna Bombica Ocean<br>Shell 160g<br>€5,50</p><span class="btn">OGLEJ SI PONUDBO</span></div>
    <div class="dots"><i></i><i></i><i></i></div></div>
  <h3 class="best">Najbolj Prodajano</h3>
</section>

<section class="desk" style="left:240px;top:510px">
  <div class="topbar"><span>info@trelk.si</span><span class="soc"><i></i><i></i></span></div>
  <nav class="nav"><span>Domov</span><span>Trgovina ▾</span><b class="logo">Trelk</b><span class="tools"><span>Vpiši se</span><span>⌕</span><span>♡<span class="badge"></span></span><span>€0,00<span class="badge"></span></span></span></nav>
  <div class="hero">
    <div class="arch"></div><div class="blob-l"></div><div class="blob-t"></div><div class="blob-r"></div>
    <div class="photo ph-balm" role="img" aria-label="Balzam za ustnice v roza lončku"></div>
    <div class="copy"><h2>Telesa In Obraza</h2><p>Balzam Za Ustnice<br>Berry Cream<br>€2,90</p><span class="btn">OGLEJ SI PONUDBO</span></div>
    <div class="dots"><i></i><i></i><i></i></div>
  </div>
  <span class="chat">Klepet</span>
</section>

<section class="desk" style="left:622px;top:510px">
  <div class="topbar"><span>info@trelk.si</span><span class="soc"><i></i><i></i></span></div>
  <nav class="nav"><span>Domov</span><span>Trgovina ▾</span><b class="logo">Trelk</b><span class="tools"><span>Vpiši se</span><span>⌕</span><span>♡<span class="badge"></span></span><span>€0,00<span class="badge"></span></span></span></nav>
  <div class="hero">
    <div class="arch"></div><div class="blob-l"></div><div class="blob-t"></div><div class="blob-r"></div>
    <div class="photo ph-soap" role="img" aria-label="Rumen trdi gel za tuširanje z roza trakom"></div>
    <div class="copy"><h2>Tuširanje</h2><p>Trdi Gel Za Tuširanje Honey Glow<br>€5,40</p><span class="btn">OGLEJ SI PONUDBO</span></div>
    <div class="dots"><i></i><i></i><i></i></div>
  </div>
  <span class="chat">Klepet</span>
</section>

<section class="mob" style="left:359px;top:724px">
  <div class="topbar"><i></i><i></i></div>
  <header class="head"><span class="burger"></span><b class="logo">Trelk</b><span class="cart"></span></header>
  <div class="hero"><div class="blob-s"></div><div class="blob-r"></div>
    <div class="photo ph-balm" role="img" aria-label="Balzam za ustnice v roza lončku"></div>
    <div class="copy"><h2>Telesa In Obraza</h2><p>Balzam Za Ustnice<br>Berry Cream<br>€2,90</p><span class="btn">OGLEJ SI PONUDBO</span></div>
    <div class="dots"><i></i><i></i><i></i></div></div>
  <h3 class="best">Najbolj Prodajano</h3>
</section>

<section class="mob" style="left:745px;top:724px">
  <div class="topbar"><i></i><i></i></div>
  <header class="head"><span class="burger"></span><b class="logo">Trelk</b><span class="cart"></span></header>
  <div class="hero"><div class="blob-s"></div><div class="blob-r"></div>
    <div class="photo ph-soap" role="img" aria-label="Rumen trdi gel za tuširanje z roza trakom"></div>
    <div class="copy"><h2>Tuširanje</h2><p>Trdi Gel Za Tuširanje Honey Glow<br>€5,40</p><span class="btn">OGLEJ SI PONUDBO</span></div>
    <div class="dots"><i></i><i></i><i></i></div></div>
  <h3 class="best">Najbolj Prodajano</h3>
</section>

</body>
</html>
```